Online Psychology Practice needs business cards.

Online Psychology service needs business cards. Have own logo- please see uploaded. I have other file formats if you need (not sure one needed?)

Details for Business Card:
Fiona Kettlewood
Clinical Psychologist BPsych, BPsych (Hons), MPsych (Clin), MAPS
T: 0457260714 | F: 08 71526804
E: hello@harbourlightmindcarestudio.com.au
W: harbourlightmindcarestudio.com.au

Industry/Entity Type

Health

Contact Information for Business Card

Logo plus details above (couldn't write in this section)

```html
<!DOCTYPE html>
<html lang="en">
<head>
<meta charset="utf-8">
<title>Harbourlight Mindcare Studio – Business Cards</title>
<link href="https://fonts.googleapis.com/css2?family=Cinzel:wght@600&family=Open+Sans:wght@400&display=swap" rel="stylesheet">
<style>
  :root {
    --page-bg: #2a2a2c;
    --card-bg: #0d0d0e;
    --card-edge: #1a1a1c;
    --brand-blue: #1c86bd;
    --text-grey: #b9bcc0;
    --rule-grey: #4a4d52;
    --silver: #d6d8db;
  }
  * { box-sizing: border-box; margin: 0; padding: 0; }
  html, body {
    width: 1200px; height: 900px; overflow: hidden;
    background: var(--page-bg);
  }
  .sheet {
    width: 1200px; height: 900px;
    display: flex; flex-direction: column; align-items: center; justify-content: center;
    gap: 44px;
  }
  .card {
    position: relative;
    width: 680px; height: 378px;
    border-radius: 22px;
    background: radial-gradient(ellipse at 60% 20%, #161618 0%, var(--card-bg) 70%);
    border: 1px solid var(--card-edge);
    overflow: hidden;
  }

  /* Front */
  .brand {
    position: absolute; left: 196px; top: 62px;
    display: flex; align-items: center; gap: 18px;
  }
  .brand-dot {
    width: 64px; height: 64px; border-radius: 50%;
    background: var(--brand-blue);
  }
  .brand-name {
    font-family: "Cinzel", serif; font-weight: 600;
    font-size: 24px; line-height: 1.2; letter-spacing: 1px;
    color: var(--brand-blue);
  }
  .divider-long {
    position: absolute; left: 290px; right: 40px; top: 170px; height: 1px;
    background: linear-gradient(to right, transparent, var(--rule-grey) 30%, var(--rule-grey));
  }
  .person { position: absolute; left: 48px; top: 186px; }
  .person-name {
    font-family: "Cinzel", serif; font-weight: 600;
    font-size: 27px; letter-spacing: 1px; color: var(--brand-blue);
  }
  .person-title {
    font-family: "Open Sans", sans-serif; font-size: 15px; line-height: 20px;
    color: var(--text-grey); margin-top: 2px;
  }
  .divider-short {
    position: absolute; left: 48px; width: 280px; top: 262px; height: 1px;
    background: var(--rule-grey);
  }
  .contacts {
    position: absolute; left: 48px; top: 272px;
    list-style: none;
    font-family: "Open Sans", sans-serif; font-size: 15px; line-height: 22px;
    color: var(--text-grey);
  }
  .contacts li { display: flex; align-items: center; gap: 10px; }
  .contacts svg { width: 15px; height: 15px; flex: none; fill: var(--brand-blue); }

  /* Back */
  .card-back { display: flex; align-items: center; justify-content: center; }
  .brand-back { display: flex; flex-direction: column; align-items: center; gap: 22px; }
  .brand-back .brand-dot { width: 92px; height: 92px; background: var(--silver); }
  .brand-back .brand-name {
    color: var(--silver); font-size: 30px; text-align: center;
  }
</style>
</head>
<body>
<main class="sheet">

  <section class="card card-front">
    <div class="brand">
      <span class="brand-dot"></span>
      <p class="brand-name">Harbourlight<br>Mindcare Studio</p>
    </div>
    <div class="divider-long"></div>

    <div class="person">
      <h1 class="person-name">FIONA KETTLEWOOD</h1>
      <p class="person-title">Clinical Psychologist BPsych<br>BPsych (Hons), MPsych (Clin), MAPS</p>
    </div>
    <div class="divider-short"></div>

    <ul class="contacts">
      <li>
        <svg viewBox="0 0 24 24" aria-hidden="true"><path d="M6.6 10.8a15.1 15.1 0 0 0 6.6 6.6l2.2-2.2a1 1 0 0 1 1-.25 11.4 11.4 0 0 0 3.6.57 1 1 0 0 1 1 1V20a1 1 0 0 1-1 1A17 17 0 0 1 3 4a1 1 0 0 1 1-1h3.5a1 1 0 0 1 1 1c0 1.25.2 2.45.57 3.57a1 1 0 0 1-.25 1z"/></svg>
        0457260714
      </li>
      <li>
        <svg viewBox="0 0 24 24" aria-hidden="true"><path d="M7 3h10v4H7zM4 8h16a2 2 0 0 1 2 2v6h-4v5H6v-5H2v-6a2 2 0 0 1 2-2zm4 8v3h8v-3z"/></svg>
        08 71526804
      </li>
      <li>
        <svg viewBox="0 0 24 24" aria-hidden="true"><path d="M2 5h20v14H2zm2 2v.5l8 5 8-5V7zm0 2.8V17h16V9.8l-8 5z"/></svg>
        hello@harbourlightmindcarestudio.com.au
      </li>
      <li>
        <svg viewBox="0 0 24 24" aria-hidden="true"><path d="M12 2a10 10 0 1 0 0 20 10 10 0 0 0 0-20zm6.9 6h-3a15 15 0 0 0-1.3-3.9A8 8 0 0 1 18.9 8zM12 4a13 13 0 0 1 1.9 4h-3.8A13 13 0 0 1 12 4zM4.3 14a8 8 0 0 1 0-4h3.4a16 16 0 0 0 0 4zm.8 2h3a15 15 0 0 0 1.3 3.9A8 8 0 0 1 5.1 16zm3-8h-3a8 8 0 0 1 4.3-3.9A15 15 0 0 0 8.1 8zM12 20a13 13 0 0 1-1.9-4h3.8A13 13 0 0 1 12 20zm2.3-6H9.7a14 14 0 0 1 0-4h4.6a14 14 0 0 1 0 4zm.3 5.9a15 15 0 0 0 1.3-3.9h3a8 8 0 0 1-4.3 3.9zm1.7-5.9a16 16 0 0 0 0-4h3.4a8 8 0 0 1 0 4z"/></svg>
        harbourlightmindcarestudio.com.au
      </li>
    </ul>
  </section>

  <section class="card card-back">
    <div class="brand-back">
      <span class="brand-dot"></span>
      <p class="brand-name">Harbourlight<br>Mindcare Studio</p>
    </div>
  </section>

</main>
</body>
</html>
```